Chor bzw. Vocalensemble
Konzertplakat - Handzettel
Titel: Die Kehlkränzchen gibt ein Mordskonzert
Ort: Tettnang im Lindenhalle
Datum: 24.10.2015 20.00 Uhr
Es sollte auf jeden Fall erkennbar sein, dass es sich um ein Chorkonzert handelt.
Lieder sind alle zum Thema Verbrechen aber eher im zweideutigen Sinn.
Schon allein das Thema des Konzerts ist zweideutig zu verstehen.
Bei "Wobble Wobble" wird z.Bsp. eine Fliege in der Suppe gefunden...Jim Parkin wird einer erhängt, Nebelwalzr zwielichtige Barszene, bei der "Lauen Abend" erleidet jemand einen Gedächnisverlust, River sighs versinnbildlich Blättersterben (Herbst).
Wir könnten uns aber auch ein "retromäßiges" Plakat vorstellen, im Stil Gangsterzeit wie sie gut zum Nebelwalzer passt.
Wir werden Bilder anfügen, die eventuell auch nochmal überarbeitet werden müssen, weil sie ziemlich hell sind. Aber das können wir nach Auswahl noch machen. Die sind nicht zwingend einzusetzen, könnten aber mit eingebaut werden.
Wir sind offen für alles und sehr gespannt auf die Entwürfe.

```html
<!DOCTYPE html>
<html lang="de">
<head>
<meta charset="utf-8">
<title>Die Kehlkränzchen gibt ein Mordskonzert</title>
<link href="https://fonts.googleapis.com/css2?family=Rubik+Wet+Paint&family=Permanent+Marker&family=Rubik+Dirt&display=swap" rel="stylesheet">
<style>
  :root {
    --ink: #0a0a0a;
    --blood: #c8070d;
    --blood-deep: #7a0306;
    --blood-bright: #e0141a;
    --paper: #f2f2f2;
    --chalk: #d9d9d9;
  }
  html, body {
    margin: 0;
    padding: 0;
    overflow: hidden;
    background: var(--ink);
  }
  .poster {
    position: relative;
    width: 872px;
    height: 1200px;
    overflow: hidden;
    background: var(--ink);
  }
  .poster-backdrop {
    position: absolute;
    inset: 0;
  }
  .title-block {
    position: absolute;
    inset: 0;
    margin: 0;
    font-size: inherit;
  }
  .title {
    position: absolute;
    display: block;
    color: var(--blood-bright);
    font-family: "Rubik Wet Paint", cursive;
    font-weight: 400;
    text-transform: uppercase;
    text-shadow: 0 0 8px rgba(255,255,255,0.55), 2px 2px 0 var(--paper);
    line-height: 1;
    white-space: nowrap;
    transform-origin: left center;
  }
  .title-choir {
    left: 170px;
    top: 95px;
    font-size: 40px;
    transform: rotate(-7deg);
  }
  .title-verb {
    left: 330px;
    top: 158px;
    font-size: 36px;
    transform: rotate(-5deg);
  }
  .title-main {
    left: 105px;
    top: 262px;
    font-size: 74px;
    transform: rotate(-7deg);
  }
  .tagline {
    position: absolute;
    margin: 0;
    left: 66px;
    color: var(--paper);
    font-family: "Permanent Marker", "Arial Black", sans-serif;
    text-transform: uppercase;
    line-height: 1;
    white-space: nowrap;
    transform: rotate(3deg);
    transform-origin: left center;
  }
  .tagline-danger { top: 340px; font-size: 38px; }
  .tagline-mystery { top: 402px; font-size: 28px; }
  .tagline-romance { top: 448px; font-size: 21px; }
  .event-details {
    position: absolute;
    left: 74px;
    top: 945px;
    margin: 0;
    color: var(--chalk);
    font-family: "Rubik Dirt", sans-serif;
    font-size: 38px;
    line-height: 1;
    text-transform: uppercase;
    transform: rotate(-4deg);
    transform-origin: left top;
  }
  .event-details p {
    margin: 0 0 28px 0;
    white-space: nowrap;
  }
</style>
</head>
<body>
<main class="poster">
  <svg class="poster-backdrop" width="872" height="1200" viewBox="0 0 872 1200">
    <defs>
      <radialGradient id="bloodGlow" cx="0.55" cy="0.35" r="0.8">
        <stop offset="0" stop-color="#e0141a"/>
        <stop offset="0.6" stop-color="#b5060b"/>
        <stop offset="1" stop-color="#5e0204"/>
      </radialGradient>
      <linearGradient id="photoTone" x1="0" y1="0" x2="1" y2="1">
        <stop offset="0" stop-color="#d6d6d6"/>
        <stop offset="0.5" stop-color="#8a8a8a"/>
        <stop offset="1" stop-color="#3a3a3a"/>
      </linearGradient>
      <linearGradient id="bandTone" x1="0" y1="0" x2="1" y2="0">
        <stop offset="0" stop-color="#e0141a"/>
        <stop offset="1" stop-color="#9a0408"/>
      </linearGradient>
    </defs>

    <path class="blood-wash" fill="url(#bloodGlow)"
      d="M300 0 L872 0 L872 830 L820 860 L760 840 L700 870 L40 880 L30 820 L20 330 L70 300 L120 250 L160 200 L240 160 L250 90 L280 40 Z"/>
    <path fill="var(--blood-deep)" d="M720 30 L790 10 L830 50 L800 80 L750 70 Z"/>
    <path fill="var(--ink)" d="M0 0 L300 0 L260 60 L240 150 L160 190 L90 240 L30 320 L0 330 Z"/>

    <path fill="var(--blood)" opacity="0.85"
      d="M40 880 L700 870 L760 900 L720 960 L600 990 L420 1000 L200 980 L60 960 Z"/>
    <path class="details-band" fill="url(#bandTone)"
      d="M30 1005 L860 985 L872 1010 L872 1130 L820 1150 L600 1160 L300 1170 L40 1165 L20 1120 Z"/>

    <g class="staff-lines" stroke="var(--blood-deep)" stroke-width="2" opacity="0.7">
      <line x1="30" y1="395" x2="860" y2="395"/><line x1="30" y1="405" x2="860" y2="405"/>
      <line x1="30" y1="415" x2="860" y2="415"/><line x1="30" y1="425" x2="860" y2="425"/>
      <line x1="30" y1="435" x2="860" y2="435"/>
      <line x1="30" y1="785" x2="860" y2="785"/><line x1="30" y1="795" x2="860" y2="795"/>
      <line x1="30" y1="805" x2="860" y2="805"/><line x1="30" y1="815" x2="860" y2="815"/>
      <line x1="30" y1="825" x2="860" y2="825"/>
      <line x1="30" y1="880" x2="860" y2="880"/><line x1="30" y1="890" x2="860" y2="890"/>
      <line x1="30" y1="900" x2="860" y2="900"/><line x1="30" y1="910" x2="860" y2="910"/>
      <line x1="30" y1="920" x2="860" y2="920"/>
    </g>

    <g class="photo-strip">
      <path fill="var(--paper)"
        d="M220 362 L310 342 L400 352 L470 340 L560 350 L640 330 L720 352 L790 340 L855 362 L858 474 L780 490 L700 482 L620 500 L540 475 L460 490 L380 470 L300 478 L222 465 Z"/>
      <path role="img" aria-label="Schwarzweißfoto der fünf Männerstimmen des Chors" fill="url(#photoTone)"
        d="M230 368 L310 350 L400 360 L470 348 L560 358 L640 338 L720 360 L790 348 L850 368 L852 466 L780 482 L700 474 L620 492 L540 467 L460 482 L380 462 L300 470 L232 458 Z"/>
    </g>
    <g class="photo-strip">
      <path fill="var(--paper)"
        d="M34 590 L110 570 L220 560 L300 575 L380 550 L470 565 L560 545 L650 560 L740 540 L820 548 L842 600 L838 720 L760 725 L660 715 L560 740 L460 720 L360 745 L260 735 L150 750 L34 725 Z"/>
      <path role="img" aria-label="Schwarzweißfoto der sieben Frauenstimmen des Chors" fill="url(#photoTone)"
        d="M40 596 L110 578 L220 568 L300 583 L380 558 L470 573 L560 553 L650 568 L740 548 L816 556 L834 602 L830 712 L760 717 L660 707 L560 732 L460 712 L360 737 L260 727 L150 742 L40 717 Z"/>
    </g>
  </svg>

  <h1 class="title-block">
    <span class="title title-choir">Die Kehlkränzchen</span>
    <span class="title title-verb">gibt ein</span>
    <span class="title title-main">Mordskonzert</span>
  </h1>

  <p class="tagline tagline-danger">Danger</p>
  <p class="tagline tagline-mystery">Mystery</p>
  <p class="tagline tagline-romance">Romance</p>

  <div class="event-details">
    <p class="event-place">Ort : Tettnang im Lindenhalle</p>
    <p class="event-date">Datum : 24.10.2015</p>
    <p class="event-time">Um:20:00 Uhr</p>
  </div>
</main>
</body>
</html>
```